New homepage for a digital cleaning company

We are Kelmar Tidy Works. A company that provides other companies (mostly restaurants, hotels, gas stations) with cleaning products and a mobile app to register daily, weekly, monthly tasks that they have to complete in order to meet cleaning regulation in Europe. We now have a website www.kelmartidyworks.example. This website is not optimized for the right goals. We offer this service as a subscription. There are three subsciption types people can choose from. We would like a clean, modern and professional website that also functions as a webshop. Please consider recommending a wordpress theme, we are working with visual composer.
Our app is mostly used on tablets.
We have three subsciptions: 1 dashboard of 6 products = premium = 100 eur
1 dashboard of 4 products = professional = 90 eur
1 dashboard of 3 products = basic = 85 eur
We would like a homepage designed + product page + subsciption page + how it works page + functionalities of the app page. (if possible also the about us and contact page).
Target Market(s)
gas stations, restaurants, hotels,... All companies that have to deal with HACCP regulation of hygiene.
Industry/Entity Type
Cleaning Service
Number of Pages Required
3 page
Requirements
Nice to have
- Recommended wordpress theme

```html
<!DOCTYPE html>
<html lang="en">
<head>
<meta charset="utf-8">
<title>Kelmar Tidy Works – Homepage</title>
<link href="https://fonts.googleapis.com/css2?family=Mulish:ital,wght@0,400;0,600;0,700;0,800;1,400&display=swap" rel="stylesheet">
<style>
:root{
  --blue:#1f9fe6;
  --cyan:#4fd3f6;
  --sky:#8fe0fb;
  --orange:#f7941d;
  --ink:#222a33;
  --text:#6b7480;
  --muted:#9aa3ad;
  --line:#e8edf2;
  --soft:#f6f8fa;
  --white:#ffffff;
}
*{box-sizing:border-box;margin:0;padding:0}
html,body{width:1200px;height:3571px;overflow:hidden}
body{position:relative;background:var(--white);font-family:"Mulish",Arial,sans-serif;color:var(--text)}
.abs{position:absolute}
.backdrop{position:absolute;left:0;top:0;width:1200px;height:3571px}
.logo{position:absolute;font-weight:800;color:var(--blue);font-size:22px;line-height:1.1;letter-spacing:-0.3px}
.logo .dot{display:inline-block;width:12px;height:12px;border-radius:50%;background:var(--blue);margin-right:8px;vertical-align:2px}
.nav{position:absolute;top:50px;left:552px;display:flex;gap:0;align-items:center;font-size:11px;font-weight:700;letter-spacing:1px;color:var(--white)}
.nav a{color:var(--white);text-decoration:none;margin-right:44px}
.nav a.active{text-decoration:underline;text-underline-offset:5px}
.cart{width:28px;height:28px;border:1.5px solid var(--white);border-radius:50%;display:flex;align-items:center;justify-content:center}
.eyebrow{position:absolute;font-size:10px;font-weight:800;letter-spacing:1.5px;color:var(--blue);text-transform:uppercase}
.h-display{position:absolute;color:var(--ink);font-weight:600;font-size:34px;line-height:1.22;letter-spacing:-0.3px}
.body-copy{position:absolute;font-size:13px;line-height:1.65;color:var(--text)}
.btn{position:absolute;display:flex;align-items:center;justify-content:center;font-size:10px;font-weight:800;letter-spacing:1.2px;text-transform:uppercase;height:40px}
.btn-solid{background:var(--orange);color:var(--white)}
.btn-line{border:1.5px solid var(--orange);color:var(--orange);background:var(--white)}
.btn-line-blue{border:1.5px solid var(--sky);color:var(--blue)}
.btn-blue{background:var(--blue);color:var(--white)}
.phone{position:absolute;border-radius:38px;background:var(--white);box-shadow:0 20px 50px rgba(20,90,140,.18);border:3px solid #f1f4f7}
.phone-screen{position:absolute;left:14px;right:14px;top:30px;bottom:30px;border-radius:18px;background:linear-gradient(180deg,#58d1f7,#2fb0ef);overflow:hidden}
.feature-card{position:absolute;top:840px;width:280px;height:343px;background:var(--white);box-shadow:0 8px 28px rgba(30,60,90,.08);text-align:center}
.feature-icon{width:120px;height:120px;border-radius:50%;border:1.5px solid var(--line);margin:33px auto 0;display:flex;align-items:center;justify-content:center}
.feature-card h3{font-size:16px;color:var(--ink);font-weight:700;margin-top:42px}
.feature-card p{font-size:12px;line-height:1.6;margin:12px 36px 0}
.feature-card .more{display:inline-block;margin-top:30px;font-size:10px;font-weight:800;letter-spacing:1.2px;color:var(--blue);border-bottom:1.5px solid var(--blue);padding-bottom:5px}
.feature-card .more.hot{color:var(--orange);border-color:var(--orange)}
.h-sub{position:absolute;color:var(--ink);font-weight:700;font-size:16px}
.product-card{position:absolute;top:1667px;width:203px;height:319px;background:var(--white);box-shadow:0 8px 28px rgba(30,60,90,.08);text-align:center}
.product-img{position:absolute;left:36px;right:36px;top:22px;height:220px;border-radius:10px}
.product-card span{position:absolute;left:0;right:0;top:262px;font-size:13px;font-weight:600;color:var(--ink)}
.price-card{position:absolute;top:2143px;height:238px;text-align:center;border-right:1px solid var(--line);background:var(--white)}
.price-card.last{border-right:none}
.tier{display:block;margin-top:38px;font-size:10px;font-weight:800;letter-spacing:1.5px;color:var(--cyan)}
.price{display:block;margin-top:14px;font-size:44px;color:var(--cyan);font-weight:400;line-height:1}
.price small{font-size:24px}
.price.pro{color:var(--blue)}
.price.prem{color:var(--orange)}
.rule{width:54px;height:1px;background:var(--line);margin:16px auto 0}
.plan-detail{display:block;margin-top:14px;font-size:10px;letter-spacing:1px;color:var(--text);font-weight:600}
.plan-detail b{color:var(--ink)}
.price-card .btn{position:relative;margin:18px auto 0;width:128px;height:36px}
.quote{position:absolute;left:270px;width:660px;top:2571px;text-align:center;font-style:italic;font-size:14px;line-height:1.6;color:var(--text)}
.download{position:absolute;left:0;top:2810px;width:1200px;height:321px;background:linear-gradient(90deg,#5cc9f6 0%,#7dd5f8 55%,#c9eefc 100%)}
.footer-h{position:absolute;font-size:11px;font-weight:800;letter-spacing:1.5px;color:var(--blue);text-transform:uppercase}
.footer-list{position:absolute;list-style:none;font-size:12px;line-height:29px;color:var(--text)}
.footer-list li.hot{color:var(--orange)}
.social{position:absolute;width:26px;height:26px;border:1.5px solid var(--line);border-radius:50%}
</style>
</head>
<body>

<svg class="backdrop" viewBox="0 0 1200 3571" aria-hidden="true">
  <defs>
    <linearGradient id="heroBlue" x1="0" y1="0" x2="1" y2="1">
      <stop offset="0" stop-color="#7fe4fb"/>
      <stop offset="1" stop-color="#2fb6f2"/>
    </linearGradient>
  </defs>
  <path d="M1200 1250 C1100 1180 900 1130 760 1160 C620 1190 520 1340 500 1500 C470 1750 520 2050 380 2250 C260 2420 80 2460 0 2700 L0 2810 L1200 2810 Z" fill="var(--soft)"/>
  <path d="M520 0 C540 90 600 150 700 170 C820 195 900 240 920 330 C945 450 1040 520 1200 540 L1200 0 Z" fill="url(#heroBlue)"/>
  <path d="M0 560 C110 520 240 560 250 700 C262 860 320 960 380 1030 C250 1010 120 990 0 1000 Z" fill="url(#heroBlue)"/>
  <circle cx="150" cy="1260" r="12" fill="none" stroke="var(--orange)" stroke-width="4"/>
  <circle cx="380" cy="1245" r="5" fill="#f26d7d"/>
  <circle cx="120" cy="1430" r="5" fill="#7aa8e8"/>
  <circle cx="455" cy="1420" r="4" fill="var(--blue)"/>
</svg>

<!-- Header -->
<div class="logo" style="left:157px;top:36px">Kelmar<br>Tidy Works</div>
<nav class="nav">
  <a class="active">HOME</a><a>ABOUT US</a><a>PRODUCT</a><a>SUBSCRIPTION</a><a>CONTACT</a>
  <span class="cart"><svg width="14" height="14" viewBox="0 0 14 14"><path d="M1 2h2l2 7h6l2-5H4" fill="none" stroke="#fff" stroke-width="1.4"/><circle cx="6" cy="12" r="1" fill="#fff"/><circle cx="10.5" cy="12" r="1" fill="#fff"/></svg></span>
</nav>

<!-- Hero -->
<h1 class="h-display" style="left:157px;top:225px;width:330px">Haccp Paper - work is a Thing of The Past!</h1>
<p class="body-copy" style="left:157px;top:376px;width:300px">Kelmar Tidy Works is a service in the form of monthly contracts, which originated from the needs of companies that want to clean and maintain more efficiently.</p>
<div class="btn btn-line" style="left:157px;top:486px;width:158px">Request an offer</div>
<div class="btn btn-solid" style="left:333px;top:486px;width:120px">Contact us</div>

<div class="phone" style="left:719px;top:95px;width:324px;height:583px">
  <div class="phone-screen">
    <div role="img" aria-label="Mascot illustration of a cartoon fox hero in a blue cape" class="abs" style="left:50px;top:145px;width:190px;height:190px;border-radius:50%;background:rgba(255,255,255,.25)"></div>
    <div class="abs" style="left:0;right:0;bottom:0;height:60px;background:var(--white);border-radius:50% 50% 0 0/40% 40% 0 0"></div>
    <div class="abs" style="left:0;right:0;bottom:12px;text-align:center;font-size:10px;font-weight:700;color:var(--ink)">www.kelmartidyworks.example</div>
  </div>
</div>

<!-- Why choose us -->
<div class="eyebrow" style="left:0;width:1200px;text-align:center;top:692px">Why choose us</div>
<h2 class="h-display" style="left:0;width:1200px;text-align:center;top:775px;font-size:32px">Kelmar Tidy Works</h2>

<div class="feature-card" style="left:157px">
  <div class="feature-icon"><svg width="56" height="56" viewBox="0 0 56 56"><rect x="12" y="8" width="30" height="40" rx="3" fill="none" stroke="var(--blue)" stroke-width="2"/><path d="M18 18h18M18 25h18M18 32h12" stroke="var(--orange)" stroke-width="2"/><path d="M36 40l12-12" stroke="var(--blue)" stroke-width="3"/></svg></div>
  <h3>No More Paperwork</h3>
  <p>For the employee: From simplicity to pleasure, a green tick appears immediately. For the ...</p>
  <span class="more">Explore more</span>
</div>
<div class="feature-card" style="left:460px">
  <div class="feature-icon"><svg width="56" height="56" viewBox="0 0 56 56"><rect x="10" y="18" width="14" height="30" rx="3" fill="none" stroke="var(--orange)" stroke-width="2"/><rect x="30" y="14" width="14" height="34" rx="3" fill="none" stroke="var(--blue)" stroke-width="2"/><path d="M14 12h6v6h-6zM34 8h6v6h-6z" fill="none" stroke="var(--orange)" stroke-width="2"/><path d="M10 30h14M30 30h14" stroke="#f3c623" stroke-width="2"/></svg></div>
  <h3>Doing &nbsp;Business Honestly</h3>
  <p>For the employer: Work with fair cleaning products, which stimulate the senses positively ...</p>
  <span class="more hot">Explore more</span>
</div>
<div class="feature-card" style="left:764px">
  <div class="feature-icon"><svg width="56" height="56" viewBox="0 0 56 56"><path d="M28 8c6 9 10 14 10 19a10 10 0 0 1-20 0c0-5 4-10 10-19z" fill="none" stroke="var(--blue)" stroke-width="2"/><path d="M8 44c8-6 16-4 22 0h12" fill="none" stroke="var(--blue)" stroke-width="2"/></svg></div>
  <h3>Safe and Hygienic</h3>
  <p>The 2 keys to success: From physical safety to social safety, customer oriented working in ...</p>
  <span class="more">Explore more</span>
</div>

<!-- About -->
<div role="img" aria-label="Illustration of the fox mascot hero with speech bubbles and smiley icons" class="abs" style="left:175px;top:1290px;width:290px;height:300px;border-radius:40%;background:linear-gradient(160deg,#f7c08a,#5aa8e6)"></div>
<div class="eyebrow" style="left:612px;top:1265px">About us</div>
<h2 class="h-display" style="left:612px;top:1283px;font-size:32px">What are We Doing</h2>
<p class="body-copy" style="left:612px;top:1344px;width:430px;font-size:12px">Kelmar Tidy Works offers employees, managers and managements a total package for cleaning, maintenance and HACCP registration. By registering all the cleaning tasks in our app, there is no need for paperwork anymore. Simple and fast.</p>
<div class="h-sub" style="left:612px;top:1435px;font-size:18px;font-weight:600">Haccp Ready</div>
<p class="body-copy" style="left:612px;top:1470px;width:430px;font-size:12px">All your employees have an unambiguous way of working, the tasks are predefined and are executed daily. In this way all HACCP requirements are assured in the daily procedure ...</p>
<div class="btn btn-solid" style="left:612px;top:1545px;width:143px">Discover more</div>

<!-- Products -->
<div class="eyebrow" style="left:157px;top:1666px">Shop online</div>
<h2 class="h-display" style="left:157px;top:1685px;font-size:32px">Our Products</h2>
<p class="body-copy" style="left:157px;top:1748px;width:240px;font-size:12px">Clean and safe payment, a hygienic visit to the toilet, tasty food and drinks at clean tables and counters, you feel completely safe at the location. It feels like home, it smells like home and it's just your home.</p>
<svg class="abs" style="left:157px;top:1890px" width="60" height="18" viewBox="0 0 60 18"><path d="M10 3L3 9l7 6" fill="none" stroke="var(--muted)" stroke-width="1.6"/><path d="M45 3l7 6-7 6" fill="none" stroke="var(--blue)" stroke-width="1.6"/></svg>
<div class="btn btn-line" style="left:157px;top:1948px;width:160px;height:38px">View all products</div>

<div class="product-card" style="left:460px">
  <div role="img" aria-label="Product photo of a white cleaning bottle" class="product-img" style="background:linear-gradient(180deg,#eef2f5,#c9d8e6)"></div>
  <span>Refuse Refuse Bin</span>
</div>
<div class="product-card" style="left:686px">
  <div role="img" aria-label="Product photo of a drain unblocker bottle" class="product-img" style="background:linear-gradient(180deg,#f2eef1,#cfdcea)"></div>
  <span style="color:var(--blue)">Drain Unblocker</span>
</div>
<div class="product-card" style="left:914px">
  <div role="img" aria-label="Product photo of a black wall-mounted tablet dashboard stand" class="product-img" style="background:linear-gradient(180deg,#e9ecef,#3a3d42)"></div>
  <span>Professional Dashboard</span>
</div>

<!-- Pricing -->
<div class="eyebrow" style="left:0;width:1200px;text-align:center;top:2064px">Subscription</div>
<h2 class="h-display" style="left:0;width:1200px;text-align:center;top:2083px;font-size:32px">Pricing Plan</h2>
<div class="price-card" style="left:233px;width:243px">
  <span class="tier">BASIC</span>
  <span class="price">€ 85 <small>/ mo.</small></span>
  <div class="rule"></div>
  <span class="plan-detail">1 DASHBOARD OF <b>3 PRODUCTS</b></span>
  <div class="btn btn-line-blue">Get started</div>
</div>
<div class="price-card" style="left:476px;width:250px;box-shadow:0 8px 28px rgba(30,60,90,.08)">
  <span class="tier" style="color:var(--blue)">PROFESSIONAL</span>
  <span class="price pro">€ 90 <small>/ mo.</small></span>
  <div class="rule"></div>
  <span class="plan-detail">1 DASHBOARD OF <b>4 PRODUCTS</b></span>
  <div class="btn btn-blue">Get started</div>
</div>
<div class="price-card last" style="left:726px;width:245px">
  <span class="tier" style="color:var(--orange)">PREMIUM</span>
  <span class="price prem">€ 100 <small>/ mo.</small></span>
  <div class="rule"></div>
  <span class="plan-detail">1 DASHBOARD OF <b>6 PRODUCTS</b></span>
  <div class="btn btn-line">Get started</div>
</div>

<!-- Testimonial -->
<div role="img" aria-label="Portrait photo of the reviewer" class="abs" style="left:562px;top:2467px;width:76px;height:76px;border-radius:50%;background:linear-gradient(180deg,#c9a58a,#7a5a48)"></div>
<svg class="abs" style="left:155px;top:2588px" width="12" height="18" viewBox="0 0 12 18"><path d="M9 2L3 9l6 7" fill="none" stroke="var(--muted)" stroke-width="1.6"/></svg>
<svg class="abs" style="left:1032px;top:2588px" width="12" height="18" viewBox="0 0 12 18"><path d="M3 2l6 7-6 7" fill="none" stroke="var(--blue)" stroke-width="1.6"/></svg>
<p class="quote">There are many variations of passages of Lorem Ipsum available, but the majority have suffered alteration in some form, by injected humour, or randomised words which don't look even slightly If you are going to use a passage of Lorem Ipsum, you need to be sure there isn't anything embarrassing hidden middle of text good work.</p>
<div class="eyebrow" style="left:0;width:1200px;text-align:center;top:2678px">Standard chunk</div>
<svg class="abs" style="left:568px;top:2714px" width="64" height="14" viewBox="0 0 64 14"><g fill="none" stroke="var(--orange)" stroke-width="1.4"><circle cx="7" cy="7" r="5" fill="var(--orange)"/><circle cx="23" cy="7" r="5"/><circle cx="39" cy="7" r="5"/><circle cx="55" cy="7" r="5"/></g></svg>

<!-- Download -->
<section class="download">
  <div class="eyebrow" style="left:157px;top:72px;color:var(--white)">Download</div>
  <h2 class="h-display" style="left:157px;top:98px;font-size:27px;color:var(--white)">Kelmar Tidy Works</h2>
  <p class="body-copy" style="left:157px;top:142px;width:350px;color:var(--white)">Contrary to popular belief, Lorem Ipsum is not simply random text. It has roots in a piece classical.</p>
  <div class="btn btn-solid" style="left:157px;top:209px;width:128px">Get the app</div>
</section>
<div role="img" aria-label="Photo of a smartphone showing the app login screen with the fox mascot" class="abs" style="left:770px;top:2770px;width:290px;height:410px;border-radius:40px;background:linear-gradient(160deg,#ffffff,#d9f2fd 60%,#5cc6f3);transform:rotate(14deg);box-shadow:0 20px 40px rgba(20,90,140,.2)"></div>

<!-- Footer -->
<div class="logo" style="left:157px;top:3232px">Kelmar<br>Tidy Works</div>
<p class="body-copy" style="left:157px;top:3310px;font-size:12px;line-height:1.5">Lindenstraat 47,<br>5211 AB Harlingen, NL</p>
<div class="abs" style="left:157px;top:3364px;font-size:19px;font-weight:700;color:var(--blue)">Call: 040-555-0182</div>
<div class="abs" style="left:157px;top:3394px;font-size:12px;color:var(--ink)">info@kelmartidyworks.example</div>

<div class="footer-h" style="left:417px;top:3240px">Quick links</div>
<ul class="footer-list" style="left:417px;top:3260px">
  <li>Home</li><li class="hot">About Us</li><li>Product</li><li>Subscription</li><li>Blog</li><li>FAQ</li><li>Contact Us</li>
</ul>
<div class="footer-h" style="left:588px;top:3240px">Learn more</div>
<ul class="footer-list" style="left:588px;top:3260px">
  <li>Terms &amp; Conditions</li><li>Terms &amp; Conditions Webshop</li><li>Disclaimer</li><li>Privacy</li>
</ul>
<div class="footer-h" style="left:840px;top:3240px">Subscribe us</div>
<div class="abs" style="left:840px;top:3274px;width:205px;height:32px;border:1px solid var(--line);font-size:11px;color:var(--muted);padding:9px 10px">Your email...</div>
<svg class="abs" style="left:1020px;top:3284px" width="12" height="12" viewBox="0 0 12 12"><path d="M1 1l10 5-10 5 2-5z" fill="var(--muted)"/></svg>
<div class="social" style="left:840px;top:3333px"></div>
<div class="social" style="left:874px;top:3333px"></div>
<div class="social" style="left:908px;top:3333px"></div>

<div class="abs" style="left:157px;top:3480px;width:886px;height:1px;background:var(--line)"></div>
<div class="abs" style="left:0;width:1200px;top:3502px;text-align:center;font-size:12px;letter-spacing:.5px;color:var(--text)">© 2018 <span style="color:var(--blue)">Kelmar Tidy Works</span>. All right reserved.</div>

</body>
</html>
```